Plakate für Konzertchor der Liederhalle Brandau
Zielgruppe
Die Liederhalle Brandau und deren Sinfonischer Chor führt chorsinfonische Werke mit Chor- und Orchester und Solisten auf. Weitere Infos unter: https://www.liederhalle-brandau.de/
Aufgabenstellung
Ein frisches und modern gestaltetes Plakat soll für das nächste Konzertprojekt entstehen. Aufgeführt wird:
Wendling As Dur Messe
Tarvik Harbor Mass
Als Gestaltungselement kommen neben Fotos vom Chor, ein Sonnenaufgang, eine Stadt oder eine Darstellung von Sphären/Weltall in Frage. Fotos vom Chor liegen in professioneller Qualität vor.
Neben dem Plakat, können Folgeaufträge für Flyer und Programmheft entstehen.
Konzertchor der Liederhalle Brandau
Kinoensemble Wendhof
Helena Markoudi, Sopran
Wiktoria Lobatsch, Alt
Friedrich Ambacher, Tenor
Udo Kessel, Tenor
Gregor Wiesner, Bass
Ortwin Haller, Dirigent
17.00 Uhr
Lindensaal Brandau

```html
<!DOCTYPE html>
<html lang="de">
<head>
<meta charset="utf-8">
<title>Geschichte Wendling – Liederhalle Brandau</title>
<link rel="stylesheet" href="https://fonts.googleapis.com/css2?family=Cinzel:wght@400&family=Tinos:wght@400&display=swap">
<style>
  :root {
    --wine: #962b36;
    --ivory: #ffffff;
    --sky-deep: #1f3050;
    --sky-mid: #4a6585;
    --gold: #d9a457;
    --sea: #2a3852;
    --shore: #3a2e36;
  }
  * { margin: 0; padding: 0; box-sizing: border-box; }
  html, body { width: 800px; height: 1200px; overflow: hidden; background: var(--wine); }
  .poster {
    position: relative;
    width: 800px;
    height: 1200px;
    overflow: hidden;
    background: var(--wine);
    color: var(--ivory);
    font-family: "Tinos", "Times New Roman", serif;
    font-weight: 400;
    text-align: center;
  }
  .masthead {
    position: absolute;
    top: 0; left: 0;
    width: 800px; height: 112px;
    display: flex; align-items: center; justify-content: center;
  }
  .masthead__name {
    font-family: "Cinzel", "Times New Roman", serif;
    font-size: 48px;
    font-weight: 400;
    line-height: 1;
    letter-spacing: 1px;
    color: var(--ivory);
    padding-top: 6px;
    white-space: nowrap;
  }
  .hero {
    position: absolute;
    top: 112px; left: 0;
    width: 800px; height: 521px;
    background: linear-gradient(to bottom,
      var(--sky-deep) 0%,
      var(--sky-mid) 30%,
      var(--gold) 50%,
      var(--sea) 68%,
      var(--shore) 100%);
  }
  .hero__title {
    position: absolute;
    left: 0; right: 0;
    top: 547px;
    font-size: 80px;
    font-weight: 400;
    line-height: 1;
    white-space: nowrap;
  }
  .programme {
    position: absolute;
    left: 0; right: 0;
    top: 642px;
    font-size: 37px;
    line-height: 1;
    white-space: nowrap;
  }
  .flourish {
    position: absolute;
    left: 340px; top: 697px;
    width: 110px; height: 42px;
    border-radius: 50%;
    background: radial-gradient(ellipse at center, rgba(255,255,255,0.4), rgba(255,255,255,0) 70%);
  }
  .credits {
    position: absolute;
    left: 0; right: 0;
    top: 755px;
    list-style: none;
    font-size: 26px;
    line-height: 35.5px;
    white-space: nowrap;
  }
  .date {
    position: absolute;
    left: 0; right: 0;
    top: 1001px;
    font-size: 66px;
    line-height: 1;
    word-spacing: 20px;
    white-space: nowrap;
  }
  .venue {
    position: absolute;
    left: 0; right: 0;
    top: 1084px;
    font-size: 55px;
    line-height: 1;
    white-space: nowrap;
  }
</style>
</head>
<body>
<main class="poster">
  <header class="masthead">
    <span class="masthead__name">LIEDERHALLE BRANDAU</span>
  </header>

  <div class="hero" role="img" aria-label="Foto: Sonnenaufgang über dem Meer mit Wolken und spiegelndem Strand"></div>
  <h1 class="hero__title">Geschichte Wendling</h1>

  <p class="programme">As Dur Messe&nbsp; und Tarvik Harbor Mass</p>

  <div class="flourish" role="img" aria-label="Ornament: verschlungene Zierlinie"></div>

  <ul class="credits">
    <li>Konzertchor der Liederhalle Brandau</li>
    <li>Kinoensemble Wendhof</li>
    <li>Helena Markoudi, Sopran</li>
    <li>Wiktoria Lobatsch, Alt, Friedrich Ambacher, Tenor</li>
    <li>Udo Kessel, Tenor, Gregor Wiesner, Bass</li>
    <li>Ortwin Haller, Dirigent</li>
  </ul>

  <p class="date">15.10.2023 17.00 Uhr</p>
  <p class="venue">Lindensaal Brandau.</p>
</main>
</body>
</html>
```